Cosmetic Dental Advert For lift in busy CBD

We need a DIRECT RESPONSE advert designed for a cosmetic dentist that is placing adverts into a building lift.

OFFICE PROVIDES BRANDS ACCESS TO REACH HIGH INCOME PROFESSIONALS WITHIN PREMIUM BUSINESS ENVIRONMENTS

We are not advertising a specific clinic so we want people to go to the website that is advertised and ask for the free initial consultation.

You can reduce the amount of words / points to make it simpler to read.

Target Market(s)

Professional at work - seeing advert in a lift or foyer

Industry/Entity Type

Dental

Colors

Designer to choose colors to be used in the design.

Requirements
Must have
• The domain "www.grinvora88.com.au" must be very strong and encourage people to visit / search for it.
• The offer is a ["FREE Initial consultation" with voucher code "grinvora88"]
• The advert must be in Vector format.
• Apply the landing page corner image bottom right
Nice to have
• Provide a Male / Female version
• Emphasize the beautiful smile like in the sample
Should not have
• Must not be busy. This is a direct response so the viewer must get the call to action in 2 seconds

```html
<!DOCTYPE html>
<html lang="en">
<head>
<meta charset="utf-8">
<title>Cosmetic Dentistry Lift Advert</title>
<link href="https://fonts.googleapis.com/css2?family=Raleway:wght@400;500;700;800&display=swap" rel="stylesheet">
<style>
  :root {
    --paper: #f6f6f7;
    --plus: #dcdcdf;
    --pink: #e46ac4;
    --blue: #2d3192;
    --magenta: #e0187f;
    --magenta-dark: #a40f5c;
    --white: #ffffff;
    --curl: #cfcfd3;
  }
  html, body {
    margin: 0;
    padding: 0;
    overflow: hidden;
    background: var(--white);
  }
  .advert {
    position: relative;
    width: 932px;
    height: 1200px;
    overflow: hidden;
    background: var(--paper);
    font-family: "Raleway", Arial, sans-serif;
  }
  .backdrop {
    position: absolute;
    inset: 0;
  }
  .model-photo {
    position: absolute;
    left: 0;
    top: 212px;
    width: 530px;
    height: 920px;
    background: radial-gradient(ellipse at 52% 22%, #d8b6a2 0%, #8a5a45 28%, #3d2a24 55%, #1e1e22 80%);
    border-radius: 240px 240px 0 0;
  }
  .headline-lead {
    position: absolute;
    left: 285px;
    top: 125px;
    width: 370px;
    margin: 0;
    text-align: center;
    color: var(--blue);
    font-weight: 500;
    font-size: 76px;
    line-height: 78px;
  }
  .headline-word {
    position: absolute;
    left: 420px;
    top: 280px;
    margin: 0;
    color: var(--white);
    font-weight: 500;
    font-size: 200px;
    line-height: 200px;
    letter-spacing: -4px;
  }
  .headline-service {
    position: absolute;
    left: 470px;
    top: 490px;
    width: 440px;
    margin: 0;
    text-align: center;
    color: var(--white);
    font-weight: 400;
    font-size: 70px;
    line-height: 76px;
  }
  .offer-ribbon {
    position: absolute;
    left: 30px;
    top: 930px;
    width: 690px;
    height: 150px;
  }
  .offer-text {
    position: absolute;
    left: 40px;
    top: 962px;
    width: 640px;
    text-align: center;
    color: var(--white);
    margin: 0;
  }
  .offer-title {
    display: block;
    font-weight: 800;
    font-size: 54px;
    line-height: 60px;
  }
  .offer-code {
    display: block;
    font-weight: 500;
    font-size: 33px;
    line-height: 38px;
  }
  .web-bar {
    position: absolute;
    left: 0;
    top: 1128px;
    width: 735px;
    height: 72px;
    background: var(--blue);
    border-radius: 0 36px 0 0;
    color: var(--white);
    font-weight: 800;
    font-size: 50px;
    line-height: 72px;
    text-align: center;
  }
  .page-corner {
    position: absolute;
    right: 0;
    bottom: 88px;
    width: 170px;
    height: 150px;
  }
  .sponsor {
    position: absolute;
    left: 752px;
    top: 1132px;
    width: 175px;
    color: var(--blue);
  }
  .sponsor-name {
    display: flex;
    align-items: center;
    gap: 6px;
    font-weight: 700;
    font-size: 30px;
    line-height: 34px;
  }
  .sponsor-dot {
    width: 14px;
    height: 14px;
    border-radius: 50%;
    background: var(--blue);
  }
  .sponsor-tagline {
    font-weight: 500;
    font-size: 10px;
    letter-spacing: 1px;
    text-transform: uppercase;
    color: var(--blue);
  }
</style>
</head>
<body>
<main class="advert">
  <svg class="backdrop" width="932" height="1200" viewBox="0 0 932 1200" aria-hidden="true">
    <g fill="var(--plus)">
      <rect x="162" y="310" width="54" height="8"/><rect x="185" y="287" width="8" height="54"/>
      <rect x="420" y="335" width="44" height="7"/><rect x="438" y="317" width="7" height="44"/>
      <rect x="495" y="228" width="44" height="7"/><rect x="513" y="210" width="7" height="44"/>
      <rect x="870" y="132" width="54" height="8"/><rect x="893" y="109" width="8" height="54"/>
      <rect x="20" y="580" width="44" height="7"/><rect x="38" y="562" width="7" height="44"/>
      <rect x="765" y="888" width="54" height="8"/><rect x="788" y="865" width="8" height="54"/>
      <rect x="660" y="1022" width="44" height="7"/><rect x="678" y="1004" width="7" height="44"/>
    </g>
    <circle cx="676" cy="520" r="312" fill="var(--blue)"/>
    <circle cx="470" cy="192" r="215" fill="var(--pink)" opacity="0.78"/>
  </svg>

  <div class="model-photo" role="img" aria-label="Portrait of a smiling professional woman in a dark blazer, arms folded"></div>

  <h1 class="headline-lead">Transform your</h1>
  <p class="headline-word">smile</p>
  <p class="headline-service">with Cosmetic Dentistry</p>

  <svg class="page-corner" viewBox="0 0 170 150" aria-hidden="true">
    <path d="M170 0 L170 150 L0 150 Q110 120 170 0 Z" fill="var(--white)"/>
    <path d="M170 0 Q110 120 0 150 Q90 70 170 0 Z" fill="var(--curl)"/>
  </svg>

  <svg class="offer-ribbon" viewBox="0 0 690 150" aria-hidden="true">
    <polygon points="560,0 620,0 620,30 560,30" fill="var(--magenta-dark)"/>
    <polygon points="0,120 60,120 60,150" fill="var(--magenta-dark)"/>
    <rect x="0" y="20" width="690" height="110" fill="var(--magenta)"/>
  </svg>
  <p class="offer-text">
    <span class="offer-title">Free initial consultation</span>
    <span class="offer-code">Voucher code “grinvora88”</span>
  </p>

  <div class="web-bar">www.grinvora88.com.au</div>

  <div class="sponsor">
    <div class="sponsor-name"><span class="sponsor-dot"></span>Dentova</div>
    <div class="sponsor-tagline">trusted care partners</div>
  </div>
</main>
</body>
</html>
```